Solar appointment reminder card

We are looking for a new design for our appointment reminder card since we have changed our logo. The card should have the new logo along with space for the employee to hand write the customers appointment date, time, the employees name and phone number.
I've uploaded what our old basic appointment card looked like and our new logo.

The cards should be in a standard business card size and could be horizontal or vertical.

```html
<!DOCTYPE html>
<html lang="en">
<head>
<meta charset="utf-8">
<title>Solrise Appointment Card</title>
<link rel="stylesheet" href="https://fonts.googleapis.com/css2?family=Montserrat:wght@600;700&family=Short+Stack&display=swap">
<style>
  :root {
    --orange: #f7931e;
    --orange-soft: #fde9b8;
    --ink: #2a2555;
    --rule: #b9b9b9;
    --card: #ffffff;
    --backdrop: #e4e4e4;
  }
  * { box-sizing: border-box; margin: 0; padding: 0; }
  html, body { width: 1200px; height: 900px; overflow: hidden; }
  body {
    background: var(--backdrop);
    font-family: "Montserrat", Arial, sans-serif;
    position: relative;
  }
  .card {
    position: absolute;
    left: 263px;
    width: 674px;
    height: 385px;
    background: var(--card);
    border-radius: 22px;
    overflow: hidden;
    box-shadow: 0 6px 16px rgba(0,0,0,0.18);
  }
  .card--blank { top: 50px; }
  .card--filled { top: 463px; }

  .card__glow {
    position: absolute;
    left: 520px;
    top: 250px;
    width: 260px;
    height: 260px;
    border-radius: 50%;
    background: var(--orange-soft);
    opacity: 0.55;
  }
  .card__footer {
    position: absolute;
    left: 0; right: 0; bottom: 0;
    height: 18px;
    background: var(--orange);
  }

  .brand {
    position: absolute;
    left: 40px;
    top: 72px;
    display: flex;
    align-items: center;
    gap: 14px;
  }
  .brand__dot {
    width: 44px; height: 44px;
    border-radius: 50%;
    background: var(--orange);
  }
  .brand__name {
    font-weight: 700;
    font-size: 46px;
    letter-spacing: -1px;
    color: var(--orange);
    line-height: 1;
  }

  .tag {
    position: absolute;
    left: 320px;
    top: 60px;
    width: 354px;
    height: 78px;
    background: var(--orange);
    border-radius: 6px 0 0 6px;
    color: #fff;
    font-weight: 700;
    font-size: 35px;
    display: flex;
    align-items: center;
    padding-left: 30px;
    letter-spacing: 0.3px;
  }

  .field {
    position: absolute;
    height: 34px;
    border-bottom: 2px dotted var(--rule);
  }
  .field__value {
    position: absolute;
    left: 26px;
    bottom: 4px;
    font-family: "Short Stack", "Comic Sans MS", cursive;
    font-size: 30px;
    color: var(--ink);
    white-space: nowrap;
    letter-spacing: 1px;
  }
  .field--date  { left: 80px;  top: 184px; width: 267px; }
  .field--time  { left: 420px; top: 184px; width: 222px; }
  .field--time .field__value { left: 10px; }
  .field--name  { left: 80px;  top: 248px; width: 562px; }
  .field--phone { left: 80px;  top: 314px; width: 562px; }

  .icon {
    position: absolute;
    width: 34px; height: 34px;
    fill: none;
    stroke: var(--orange);
    stroke-width: 2;
  }
  .icon--date  { left: 34px;  top: 186px; }
  .icon--time  { left: 375px; top: 186px; }
  .icon--name  { left: 34px;  top: 250px; }
  .icon--phone { left: 34px;  top: 316px; }
</style>
</head>
<body>

<svg width="0" height="0" style="position:absolute">
  <defs>
    <symbol id="i-calendar" viewBox="0 0 34 34">
      <rect x="2" y="5" width="30" height="27" rx="2"/>
      <line x1="2" y1="11" x2="32" y2="11"/>
      <line x1="9" y1="2" x2="9" y2="8"/>
      <line x1="25" y1="2" x2="25" y2="8"/>
      <path d="M6 15h22M6 20h22M6 25h22M11 13v16M17 13v16M23 13v16"/>
    </symbol>
    <symbol id="i-clock" viewBox="0 0 34 34">
      <circle cx="17" cy="17" r="15"/>
      <circle cx="17" cy="17" r="11.5"/>
      <path d="M17 10v8l5 4"/>
    </symbol>
    <symbol id="i-badge" viewBox="0 0 34 34">
      <rect x="2" y="7" width="30" height="24" rx="2"/>
      <rect x="13" y="2" width="8" height="6"/>
      <circle cx="10" cy="17" r="3"/>
      <path d="M5 26c0-4 2.5-5.5 5-5.5s5 1.5 5 5.5"/>
      <path d="M19 16h9M19 20h9M19 24h6"/>
    </symbol>
    <symbol id="i-phone" viewBox="0 0 34 34">
      <circle cx="17" cy="17" r="15"/>
      <path d="M11 9l3 0 2 5-2 2c1 2.5 2.5 4 5 5l2-2 5 2v3c0 1-1 2-2 2-7 0-14-7-14-14 0-1 0-3 1-3z"/>
    </symbol>
  </defs>
</svg>

<article class="card card--blank" aria-label="Appointment card, blank">
  <div class="card__glow"></div>
  <div class="brand"><span class="brand__dot"></span><span class="brand__name">SOLRISE</span></div>
  <div class="tag">APPOINTMENT</div>

  <svg class="icon icon--date"><use href="#i-calendar"/></svg>
  <div class="field field--date"></div>
  <svg class="icon icon--time"><use href="#i-clock"/></svg>
  <div class="field field--time"></div>
  <svg class="icon icon--name"><use href="#i-badge"/></svg>
  <div class="field field--name"></div>
  <svg class="icon icon--phone"><use href="#i-phone"/></svg>
  <div class="field field--phone"></div>

  <div class="card__footer"></div>
</article>

<article class="card card--filled" aria-label="Appointment card, filled in">
  <div class="card__glow"></div>
  <div class="brand"><span class="brand__dot"></span><span class="brand__name">SOLRISE</span></div>
  <div class="tag">APPOINTMENT</div>

  <svg class="icon icon--date"><use href="#i-calendar"/></svg>
  <div class="field field--date"><span class="field__value">11.10.2019</span></div>
  <svg class="icon icon--time"><use href="#i-clock"/></svg>
  <div class="field field--time"><span class="field__value">12:00 P.m.</span></div>
  <svg class="icon icon--name"><use href="#i-badge"/></svg>
  <div class="field field--name"><span class="field__value">Dana Hollis</span></div>
  <svg class="icon icon--phone"><use href="#i-phone"/></svg>
  <div class="field field--phone"><span class="field__value">555-204-3187</span></div>

  <div class="card__footer"></div>
</article>

</body>
</html>
```